Business card design needed

Our company background is that we provides transfers to and from the airport, social & corporate events, weddings.
We are also available for charter for birthday party, wine tastings, concerts, anniversary, school balls etc.
Our business cards have to reflect that we have a professional company, they are our first contact and have to stand out from the other 'players' in the market.

Industry/Entity Type

School

Contact Information for Business Card

VESTAR PTH, Teodor & Marguerite, mob: 0427 381 592, PO Box 284, Tarrow Vale WA 6172, ABN 52 614 203 178, Lic 7169/2058,

Requirements
Must have
• Telephone number: 0427 381 592
Website: www.VESTARPTH.com.au
postal address: PO Box 284, Tarrow Vale WA 6172
Licences: Lic 7169/2058

***If using the new photo (one with the bus and buildings behind it), if possible can the buildings be cropped out. Thanks
Nice to have
• would be nice to have the pics of the vehicle(s), preferred the Vel on the card but not too fussed.
Should not have
• Picture of vehicle we don't have in our fleet. (We ONLY have the Velarions and Murako Densa mini bus)

```html
<!DOCTYPE html>
<html lang="en">
<head>
<meta charset="utf-8">
<title>VESTAR PTH – Business Cards</title>
<link rel="stylesheet" href="https://fonts.googleapis.com/css2?family=Open+Sans:wght@400;600;700&display=swap">
<style>
  :root {
    --page-bg: #2b2526;
    --card-dark: #1e1f21;
    --card-dark-2: #3a3b3e;
    --photo-light: #d9d9d9;
    --photo-mid: #8a8a8a;
    --photo-dark: #2a2a2a;
    --accent: #1e9be8;
    --accent-band: #2aa0ea;
    --white: #ffffff;
    --tagline-dark: #2f3540;
  }
  * { box-sizing: border-box; margin: 0; padding: 0; }
  html, body { width: 1200px; height: 871px; overflow: hidden; }
  body {
    background: var(--page-bg);
    font-family: "Open Sans", Arial, sans-serif;
    position: relative;
  }
  .card {
    position: absolute;
    width: 600px;
    height: 366px;
    border-radius: 22px;
    overflow: hidden;
    box-shadow: 0 14px 34px rgba(0,0,0,.45);
  }

  /* ---------- Back card ---------- */
  .card--back {
    left: 110px; top: 46px;
    background: var(--card-dark);
  }
  .card--back .vehicle-photo {
    position: absolute; inset: 0;
    background:
      radial-gradient(ellipse 40% 45% at 78% 62%, rgba(110,112,116,.55), transparent 70%),
      radial-gradient(ellipse 55% 35% at 30% 55%, rgba(90,92,96,.5), transparent 70%),
      linear-gradient(180deg, var(--card-dark-2) 0%, var(--card-dark) 100%);
  }
  .card--back .brand {
    position: absolute; top: 44px; left: 0; right: 0;
    text-align: center; color: var(--white);
  }
  .brand__name {
    font-weight: 700; font-size: 38px; letter-spacing: 2px; line-height: 1;
  }
  .brand__tagline {
    font-weight: 600; font-size: 8.5px; letter-spacing: 1.6px; margin-top: 6px;
  }
  .card--back .owners {
    position: absolute; top: 128px; left: 0; right: 0;
    text-align: center; color: var(--accent);
    font-size: 24px; font-weight: 400;
  }
  .card--back .registration {
    position: absolute; right: 84px; top: 196px;
    text-align: right; color: var(--white);
    font-size: 13px; line-height: 1.45;
  }
  .tab { position: absolute; background: var(--accent); }
  .tab--right { right: 0; top: 172px; width: 44px; height: 54px; border-radius: 10px 0 0 10px; }
  .tab--left  { left: 0; top: 258px; width: 22px; height: 60px; }
  .contact {
    position: absolute; left: 42px; top: 262px;
    list-style: none; color: var(--white); font-size: 13px;
  }
  .contact li { display: flex; align-items: center; gap: 12px; height: 26px; }
  .contact svg { width: 14px; height: 14px; flex: none; }

  /* ---------- Front card ---------- */
  .card--front {
    left: 490px; top: 462px;
    background: var(--photo-mid);
  }
  .card--front .vehicle-photo {
    position: absolute; inset: 0;
    background:
      radial-gradient(ellipse 48% 40% at 55% 55%, var(--photo-dark), transparent 75%),
      linear-gradient(180deg, #5e5e5e 0%, var(--photo-light) 30%, #a8a8a8 60%, #cfcfcf 100%);
  }
  .card--front .brand {
    position: absolute; left: 70px; top: 22px;
    color: var(--accent);
  }
  .card--front .brand__name { font-size: 46px; }
  .card--front .brand__tagline { color: var(--tagline-dark); font-size: 9px; margin-top: 4px; }
  .service-band {
    position: absolute; left: 0; top: 0; width: 600px; height: 366px;
  }
  .services {
    position: absolute; list-style: none; color: var(--white);
    font-size: 15px; line-height: 1.25;
    transform: rotate(6deg); transform-origin: left top;
  }
  .services li::before { content: "•"; margin-right: 10px; }
  .services--one   { left: 38px;  top: 216px; }
  .services--two   { left: 270px; top: 234px; }
  .services--three { left: 470px; top: 270px; }
</style>
</head>
<body>

  <section class="card card--back" aria-label="Business card back">
    <div class="vehicle-photo" role="img" aria-label="Dark photo of the front of a Velarions sedan"></div>
    <div class="brand">
      <div class="brand__name">VESTAR PTH</div>
      <div class="brand__tagline">TRANSFER SERVICES</div>
    </div>
    <p class="owners">Teodor &amp; Marguerite</p>
    <p class="registration">ABN 52 614 203 178<br>Lic 7169/2058</p>
    <div class="tab tab--right"></div>
    <div class="tab tab--left"></div>
    <ul class="contact">
      <li>
        <svg viewBox="0 0 16 16"><circle cx="8" cy="8" r="7.5" fill="none" stroke="#1e9be8"/><path d="M5.5 4.5l1.5 0 .7 2-1 .8a5 5 0 0 0 2 2l.8-1 2 .7v1.5c-3.5.3-6.3-2.5-6-6z" fill="#1e9be8"/></svg>
        0427 381 592
      </li>
      <li>
        <svg viewBox="0 0 16 16"><circle cx="8" cy="8" r="7.5" fill="none" stroke="#1e9be8"/><path d="M8 3.5a3 3 0 0 0-3 3c0 2.2 3 6 3 6s3-3.8 3-6a3 3 0 0 0-3-3zm0 4.2a1.2 1.2 0 1 1 0-2.4 1.2 1.2 0 0 1 0 2.4z" fill="#1e9be8"/></svg>
        PO Box 284, Tarrow Vale WA 6172
      </li>
    </ul>
  </section>

  <section class="card card--front" aria-label="Business card front">
    <div class="vehicle-photo" role="img" aria-label="Black and white photo of a classic Velarions sedan parked under trees"></div>
    <svg class="service-band" viewBox="0 0 600 366" aria-hidden="true">
      <polygon points="0,178 600,241 600,340 0,277" fill="var(--accent-band)" opacity="0.92"/>
    </svg>
    <div class="brand">
      <div class="brand__name">VESTAR</div>
      <div class="brand__tagline">TRANSFER SERVICES</div>
    </div>
    <ul class="services services--one">
      <li>Airport transfer</li>
      <li>Social &amp; corporate events</li>
      <li>Weddings</li>
    </ul>
    <ul class="services services--two">
      <li>Birthday party shuttle</li>
      <li>Wine tastings</li>
      <li>Concerts</li>
    </ul>
    <ul class="services services--three">
      <li>Anniversary</li>
      <li>School balls</li>
    </ul>
  </section>

</body>
</html>
```